Breezy Puffs Cotton Candy

Looking for a logo design and business cards to help a 13 year old entrepreneur promote her cotton candy business.
Contact Information for Business Card
Name, Phone & Email
Colors
E54698
E96AAD
F1A4CE
F9D9EA
FCEFF6
A7469A
B969AE
D3A5CF
EDDBEB
F8F0F9
6B429C
8869AF
B7A5CE
E3DAEB
F3F0F8
Requirements
Must have
- A fun feel that is appropriate for a teenage girl selling cotton candy

```html
<!DOCTYPE html>
<html lang="en">
<head>
<meta charset="utf-8">
<title>Breezy Puffs Cotton Candy – Business Card</title>
<link rel="stylesheet" href="https://fonts.googleapis.com/css2?family=Open+Sans:wght@400;600&display=swap">
<style>
  :root {
    --hot-pink: #E54698;
    --pink: #E96AAD;
    --soft-pink: #F1A4CE;
    --blush: #F9D9EA;
    --orchid: #A7469A;
    --grape: #6B429C;
    --white: #FFFFFF;
  }
  * { margin: 0; padding: 0; box-sizing: border-box; }
  html, body { width: 887px; height: 1200px; overflow: hidden; background: var(--white); }
  body { font-family: "Open Sans", Arial, sans-serif; color: var(--grape); }
  .canvas { position: relative; width: 887px; height: 1200px; }

  .card-front { position: absolute; left: 0; top: 0; width: 887px; height: 575px; background: var(--soft-pink); }
  .front-band { position: absolute; left: 0; top: 258px; width: 887px; height: 59px; background: var(--hot-pink); }
  .front-emblem { position: absolute; left: 267px; top: 110px; width: 354px; height: 354px; }
  .front-artwork { position: absolute; left: 358px; top: 170px; width: 170px; height: 170px; }
  .front-name { position: absolute; left: 267px; top: 346px; width: 354px; text-align: center; }

  .brand-name { font-weight: 600; color: var(--grape); line-height: 1; }
  .brand-name .title { display: block; font-size: 32px; }
  .brand-name .tagline { display: block; font-size: 13px; letter-spacing: 2.5px; margin-top: 9px; }

  .card-back { position: absolute; left: 0; top: 626px; width: 887px; height: 574px; background: var(--white); }
  .back-stripe { position: absolute; left: 0; width: 887px; background: var(--pink); }
  .back-stripe.top { top: 0; height: 22px; }
  .back-stripe.bottom { bottom: 0; height: 21px; }
  .divider { position: absolute; left: 425px; top: 57px; width: 4px; height: 459px; background: var(--orchid); }

  .back-artwork { position: absolute; left: 101px; top: 139px; width: 220px; height: 220px; }
  .back-name { position: absolute; left: 40px; top: 368px; width: 344px; text-align: center; }
  .back-name .title { font-size: 40px; }
  .back-name .tagline { font-size: 16px; letter-spacing: 3px; margin-top: 12px; }

  .owner-name { position: absolute; left: 479px; top: 152px; font-size: 54px; font-weight: 400; color: var(--grape); line-height: 1.2; }
  .contact-list { position: absolute; left: 481px; top: 307px; list-style: none; }
  .contact-item { display: flex; align-items: center; height: 42px; margin-bottom: 25px; }
  .contact-icon { width: 42px; height: 42px; border-radius: 50%; background: var(--orchid); display: flex; align-items: center; justify-content: center; color: var(--white); font-size: 24px; font-weight: 600; margin-right: 14px; flex: none; }
  .contact-text { font-size: 23px; color: var(--grape); }
</style>
</head>
<body>
<div class="canvas">
  <section class="card-front">
    <div class="front-band"></div>
    <svg class="front-emblem" viewBox="0 0 354 354">
      <circle cx="177" cy="177" r="176" fill="var(--orchid)"/>
      <circle cx="177" cy="177" r="161" fill="var(--white)"/>
    </svg>
    <svg class="front-artwork" viewBox="0 0 170 170" role="img" aria-label="Cotton candy mascot illustration with hearts">
      <circle cx="85" cy="85" r="84" fill="var(--blush)"/>
    </svg>
    <div class="front-name brand-name">
      <span class="title">Breezy Puffs</span>
      <span class="tagline">COTTON CANDY</span>
    </div>
  </section>

  <section class="card-back">
    <div class="back-stripe top"></div>
    <svg class="back-artwork" viewBox="0 0 220 220" role="img" aria-label="Cotton candy mascot illustration with hearts">
      <circle cx="110" cy="110" r="107" fill="var(--blush)" stroke="var(--pink)" stroke-width="5"/>
    </svg>
    <div class="back-name brand-name">
      <span class="title">Breezy Puffs</span>
      <span class="tagline">COTTON CANDY</span>
    </div>

    <div class="divider"></div>

    <h1 class="owner-name">Breezy Puffs</h1>
    <ul class="contact-list">
      <li class="contact-item">
        <span class="contact-icon">
          <svg width="22" height="22" viewBox="0 0 24 24" aria-hidden="true">
            <path fill="var(--white)" d="M6.6 10.8c1.4 2.8 3.8 5.1 6.6 6.6l2.2-2.2c.3-.3.7-.4 1-.2 1.1.4 2.3.6 3.6.6.6 0 1 .4 1 1V20c0 .6-.4 1-1 1C10.6 21 3 13.4 3 4c0-.6.4-1 1-1h3.5c.6 0 1 .4 1 1 0 1.3.2 2.5.6 3.6.1.3 0 .7-.2 1z"/>
          </svg>
        </span>
        <span class="contact-text">+555-210-437</span>
      </li>
      <li class="contact-item">
        <span class="contact-icon">@</span>
        <span class="contact-text">breezypuffs@mail.com</span>
      </li>
    </ul>
    <div class="back-stripe bottom"></div>
  </section>
</div>
</body>
</html>
```